Real Estate Sign Project

We need a Real Estate sign that promotes the property being listed and our company and agent listing the property. The images need to be able to be swapped out so we can use the template for each listing we have. I have a sample from another company that shows what were are trying to accomplish. Would want ours to be unique using our logo and the colors in our logo. We would like to not have to use a rider. Would want agents name and phone number to be part of the 36" x 24" sign.

Industry/Entity Type

Real Estate

Requirements
Must have
• Sign dimensions are 36 inches by 24 inches (36" across and 24" up down). Use example.of.sign.we.want.jpg as the direction we want to go but with a different layout and our logo and colors. This would be just a template that we can swap out new pictures, address, price, website, agents contact info for each home we are listing. Like the idea of the pictures bleeding off the sides. Please use free stock photos for the home images as we will be changing these out for each listing. Please incorporate all info including agents info into the one sign. File must be layered so we can change the pictures, price, website, agent, etc. We use GIMP (.xcf) file

```html
<!DOCTYPE html>
<html lang="en">
<head>
<meta charset="utf-8">
<title>Listing Sign – 1842 Willow Road</title>
<link href="https://fonts.googleapis.com/css2?family=Arimo:wght@400;700&family=Questrial&display=swap" rel="stylesheet">
<style>
  :root {
    --navy: #1f3a78;
    --slate: #4a4859;
    --slate-dark: #34323f;
    --slate-light: #5d5b6b;
    --paper: #f4f4f6;
    --mist: #dcdce2;
    --ink: #111114;
    --white: #ffffff;
    --muted: #c9c8d2;
    --photo-light: #d9e0e4;
    --photo-mid: #b8c6cc;
    --photo-warm-light: #cdbfae;
    --photo-warm-dark: #8a6a50;
  }
  html, body {
    margin: 0;
    padding: 0;
    width: 1200px;
    height: 800px;
    overflow: hidden;
    background: var(--white);
  }
  .sign {
    position: relative;
    width: 1200px;
    height: 800px;
    overflow: hidden;
    background: linear-gradient(180deg, var(--white) 0%, var(--paper) 55%, var(--mist) 100%);
    font-family: "Arimo", Arial, sans-serif;
    color: var(--ink);
  }
  .backdrop {
    position: absolute;
    inset: 0;
    width: 1200px;
    height: 800px;
  }
  .brand {
    position: absolute;
    left: 92px;
    top: 78px;
    display: flex;
    align-items: center;
  }
  .brand-mark {
    display: flex;
    align-items: center;
    gap: 12px;
    padding-right: 18px;
    margin-right: 20px;
    border-right: 2px solid var(--navy);
    height: 124px;
  }
  .brand-square {
    width: 22px;
    height: 22px;
    background: var(--navy);
  }
  .brand-name {
    font-weight: 700;
    font-size: 34px;
    color: var(--navy);
    letter-spacing: 0.5px;
  }
  .brand-tagline {
    font-size: 33px;
    line-height: 40px;
    color: var(--navy);
  }
  .price-tag {
    position: absolute;
    left: 760px;
    top: 30px;
    width: 360px;
    text-align: center;
    color: var(--white);
  }
  .price-label {
    font-family: "Questrial", Arial, sans-serif;
    font-size: 30px;
  }
  .price-value {
    font-weight: 700;
    font-size: 66px;
    line-height: 1.05;
    letter-spacing: 1px;
  }
  .address {
    position: absolute;
    right: 975px;
    top: 330px;
    text-align: right;
    font-family: "Questrial", Arial, sans-serif;
    font-style: normal;
    font-size: 46px;
    line-height: 64px;
    color: var(--ink);
  }
  .divider {
    position: absolute;
    left: 282px;
    top: 275px;
    width: 2px;
    height: 295px;
    background: var(--muted);
  }
  .features {
    position: absolute;
    left: 338px;
    top: 352px;
    margin: 0;
    padding: 0;
    list-style: none;
    font-weight: 700;
    font-size: 28px;
    line-height: 39px;
  }
  .contact-band {
    position: absolute;
    left: 0;
    top: 575px;
    width: 638px;
    height: 225px;
    background: linear-gradient(180deg, var(--slate-light) 0%, var(--slate) 45%, var(--slate-dark) 100%);
    color: var(--white);
  }
  .listing-url {
    position: absolute;
    left: 75px;
    top: 42px;
    font-weight: 700;
    font-size: 25px;
  }
  .agent {
    position: absolute;
    left: 72px;
    top: 90px;
    font-size: 34px;
  }
  .agent-label {
    font-family: "Questrial", Arial, sans-serif;
    color: var(--muted);
  }
  .agent-name { font-weight: 700; }
  .agent-phone {
    position: absolute;
    left: 75px;
    top: 154px;
    font-weight: 700;
    font-size: 23px;
  }
  .photo {
    position: absolute;
  }
  .photo-hero {
    left: 638px;
    top: 140px;
    width: 562px;
    height: 430px;
    background: linear-gradient(180deg, var(--photo-light) 0%, var(--photo-mid) 100%);
  }
  .photo-bedroom {
    left: 638px;
    top: 584px;
    width: 259px;
    height: 196px;
    background: linear-gradient(135deg, var(--photo-warm-light) 0%, var(--photo-warm-dark) 100%);
  }
  .photo-interior {
    left: 912px;
    top: 584px;
    width: 288px;
    height: 196px;
    background: linear-gradient(135deg, var(--photo-warm-light) 0%, var(--photo-warm-dark) 100%);
  }
</style>
</head>
<body>
<main class="sign">
  <div class="photo photo-hero" role="img" aria-label="Exterior photo of the listed home"></div>

  <svg class="backdrop" viewBox="0 0 1200 800" aria-hidden="true">
    <defs>
      <linearGradient id="swoosh-fill" x1="0" y1="0" x2="0" y2="1">
        <stop offset="0" stop-color="#ffffff"/>
        <stop offset="1" stop-color="#ececf0"/>
      </linearGradient>
      <linearGradient id="price-fill" x1="0" y1="0" x2="0" y2="1">
        <stop offset="0" stop-color="#5a5868"/>
        <stop offset="1" stop-color="#3e3c4b"/>
      </linearGradient>
    </defs>
    <path d="M0 0 H760 C700 60 690 150 640 190 C560 250 420 250 250 240 C150 234 60 245 0 262 Z" fill="url(#swoosh-fill)"/>
    <path d="M0 262 C60 245 150 234 250 240 C420 250 560 250 640 190 L640 205 C560 268 420 268 250 258 C150 252 60 262 0 278 Z" fill="#d3d3da"/>
    <path d="M610 0 H1200 V170 H820 C760 170 720 120 690 70 C670 35 645 10 610 0 Z" fill="url(#price-fill)"/>
  </svg>

  <header class="brand">
    <div class="brand-mark">
      <span class="brand-square"></span>
      <span class="brand-name">Keystone</span>
    </div>
    <div class="brand-tagline">Real<br>Estate<br>Services</div>
  </header>

  <section class="price-tag">
    <div class="price-label">Home for sale:</div>
    <div class="price-value">$360,000</div>
  </section>

  <address class="address">1842<br>Willow<br>Road</address>
  <div class="divider"></div>
  <ul class="features">
    <li>4 Bedrooms</li>
    <li>3.5 Baths</li>
    <li>3200 Finished SF</li>
    <li>2-Car Garage</li>
  </ul>

  <section class="contact-band">
    <div class="listing-url">keystonerealestate.com/1842willow</div>
    <div class="agent"><span class="agent-label">agent:</span> <span class="agent-name">Daniel Reeves</span></div>
    <div class="agent-phone">555/214-7730</div>
  </section>

  <div class="photo photo-bedroom" role="img" aria-label="Interior photo of the master bedroom"></div>
  <div class="photo photo-interior" role="img" aria-label="Interior photo of the living area"></div>
</main>
</body>
</html>
```